QorLa Drift Bhutan Trip

This is a one-page (A5) flyer to attract sign ups for Bhutan Trip.

Target Market(s)

Young entrepreneurs (worldwide)

Requirements
Must have
• Must have "WOW" effect and attract sign ups
Nice to have
• Striking and vibrant

```html
<!DOCTYPE html>
<html lang="en">
<head>
<meta charset="utf-8">
<title>QorLa Drift Bhutan Trip</title>
<link href="https://fonts.googleapis.com/css2?family=Lato:wght@300;400;700;900&display=swap" rel="stylesheet">
<style>
  :root {
    --orange: #f5821f;
    --orange-deep: #c8612b;
    --ink: #1f1f1f;
    --muted: #666666;
    --paper: #ffffff;
    --shadow-band: #dcdcdc;
    --strip: #141414;
  }
  * { margin: 0; padding: 0; box-sizing: border-box; }
  html, body { width: 1041px; height: 1200px; overflow: hidden; background: var(--paper); }
  body { font-family: "Lato", sans-serif; color: var(--ink); }
  .flyer { position: relative; width: 1041px; height: 1200px; overflow: hidden; background: var(--paper); }
  .flyer-shapes { position: absolute; inset: 0; width: 100%; height: 100%; }
  .headline { position: absolute; left: 388px; width: 400px; text-align: center; color: #fff; white-space: nowrap; }
  .headline-kicker { top: 418px; font-size: 39px; font-weight: 700; letter-spacing: 0.5px; }
  .headline-title { top: 466px; font-size: 59px; font-weight: 300; letter-spacing: 1px; }
  .headline-date { top: 527px; font-size: 59px; font-weight: 300; letter-spacing: 1px; }
  .headline-tagline { top: 591px; font-size: 26px; font-weight: 400; line-height: 31px; }
  .offer { position: absolute; left: 76px; top: 772px; width: 520px; }
  .offer-line { font-size: 25px; font-weight: 700; line-height: 28px; letter-spacing: -0.3px; text-transform: uppercase; }
  .offer-note { font-size: 19px; font-weight: 400; color: var(--muted); margin-top: 4px; margin-left: -4px; }
  .register { margin-top: 30px; }
  .register-email { font-size: 19px; color: var(--muted); margin-top: 4px; }
  .credit-label { font-size: 19px; color: var(--muted); margin-top: 26px; }
  .brand-mark { display: flex; align-items: center; gap: 10px; margin: 14px 0 0 22px; }
  .brand-dot { width: 22px; height: 22px; border-radius: 50%; background: var(--orange); }
  .brand-name { font-size: 30px; font-weight: 900; color: var(--orange); }
  .supporters { display: flex; align-items: flex-end; gap: 22px; margin-top: 16px; }
  .supporters-label { font-size: 19px; color: var(--muted); }
  .supporter { display: flex; flex-direction: column; align-items: center; gap: 4px; font-size: 12px; font-weight: 700; color: var(--muted); }
  .supporter-shape { width: 34px; height: 34px; border-radius: 50%; background: #2d6e8e; }
  .supporter-shape.green { background: #5aa532; }
  .supporter-shape.navy { background: #1c4a7a; border-radius: 4px; }
  .highlights { position: absolute; left: 564px; top: 912px; color: #fff; }
  .highlights-title { font-size: 23px; font-weight: 700; margin-left: 25px; margin-bottom: 4px; }
  .highlights-list { list-style: none; }
  .highlights-list li { position: relative; padding-left: 25px; font-size: 20px; font-weight: 400; line-height: 32px; white-space: nowrap; }
  .highlights-list li::before { content: ""; position: absolute; left: 0; top: 10px; width: 12px; height: 12px; border-radius: 50%; background: #000; }
  .highlights-list strong { font-weight: 700; }
</style>
</head>
<body>
<main class="flyer">
  <svg class="flyer-shapes" viewBox="0 0 726 937" preserveAspectRatio="none" aria-hidden="false">
    <defs>
      <linearGradient id="photo-tones" x1="0" y1="0" x2="0" y2="1">
        <stop offset="0" stop-color="#6f9ac4"/>
        <stop offset="0.35" stop-color="#c9d6e0"/>
        <stop offset="0.6" stop-color="#8e6f5a"/>
        <stop offset="1" stop-color="#a89c8e"/>
      </linearGradient>
    </defs>
    <rect x="0" y="0" width="726" height="372" fill="url(#photo-tones)" role="img" aria-label="Photo of a red and white Bhutanese monastery with a stone courtyard under a cloudy blue sky"/>
    <rect x="0" y="925" width="300" height="12" fill="var(--strip)"/>
    <polygon points="128,332 726,332 726,498 51,498" fill="var(--shadow-band)"/>
    <polygon points="137,340 726,340 726,490 64,490" fill="var(--orange)"/>
    <polygon points="406,560 726,560 726,937 286,937 406,620" fill="var(--orange)"/>
    <polygon points="598,494 726,494 726,937 621,937 531,582 560,530" fill="var(--orange-deep)"/>
    <circle cx="406" cy="407" r="185" fill="var(--orange)"/>
  </svg>

  <p class="headline headline-kicker">QORLA ENGAGED</p>
  <h1 class="headline headline-title">BHUTAN TRIP</h1>
  <p class="headline headline-date">3-6 JULY 2017</p>
  <p class="headline headline-tagline">Sign up for a once in a lifetime<br>experience in the land of happiness!</p>

  <section class="offer">
    <p class="offer-line">Price at USD2800</p>
    <p class="offer-line">Early bird discount USD2300</p>
    <p class="offer-note">(If you sign up by 31 March 2017)</p>
    <div class="register">
      <p class="offer-line">Register now!</p>
      <p class="offer-line">Limited to 30 participants!</p>
      <p class="register-email">Email: ivy@lumenfund.org</p>
    </div>
    <p class="credit-label">Exclusively Brought To You By:</p>
    <div class="brand-mark">
      <span class="brand-dot"></span>
      <span class="brand-name">QorLa Drift</span>
    </div>
    <div class="supporters">
      <div>
        <p class="supporters-label">Supported By:</p>
      </div>
      <div class="supporter"><span class="supporter-shape"></span>Tovari</div>
      <div class="supporter"><span class="supporter-shape green"></span>Lumen Fund</div>
      <div class="supporter"><span class="supporter-shape navy"></span>Birchway</div>
    </div>
  </section>

  <section class="highlights">
    <h2 class="highlights-title">Highlights:</h2>
    <ul class="highlights-list">
      <li><strong>LEARN</strong> from Leading Social Change Makers</li>
      <li><strong>ENGAGE</strong> the community through volunteering</li>
      <li><strong>DISCOVER</strong> your inner happiness</li>
      <li><strong>SAVOUR</strong> Organic food</li>
      <li><strong>IMMERSE</strong> in traditional sports and craft</li>
      <li><strong>EXPERIENCE</strong> warm Bhutanese hospitality</li>
      <li><strong>REJUVENATE</strong> your mind, body and soul</li>
    </ul>
  </section>
</main>
</body>
</html>
```